I need a Design for 500ml Standart 2pcs aluminium can, Veralo Taste Carbonated Soft Drink. The Design must containe the leaves of mind the lime fruits, the water drops and ice cubes. The name of the brand is VERALO. The design need to be made in modern style.

Target Market(s)

Young people from age 16 to 30

```html
<!DOCTYPE html>
<html lang="en">
<head>
<meta charset="utf-8">
<title>Veralo – 500ml Can Wraps</title>
<link rel="stylesheet" href="https://fonts.googleapis.com/css2?family=Roboto:wght@400;500;700&display=swap">
<style>
  :root {
    --canvas-bg: #e9e9eb;
    --label-white: #ffffff;
    --lime-green: #4fae32;
    --lime-green-dark: #3f9827;
    --lime-band: #d4dd1c;
    --navy: #17143a;
    --sky-band: #aed3ee;
    --shadow: rgba(0, 0, 0, 0.12);
  }
  * { box-sizing: border-box; margin: 0; padding: 0; }
  html, body {
    width: 1200px;
    height: 1200px;
    overflow: hidden;
    background: var(--canvas-bg);
    font-family: "Roboto", Arial, sans-serif;
  }
  .canvas {
    position: relative;
    width: 1200px;
    height: 1200px;
  }
  .can-wrap {
    position: absolute;
    top: 280px;
    width: 460px;
    height: 640px;
    background: var(--label-white);
    border-radius: 14px;
    overflow: hidden;
    box-shadow: 0 18px 40px var(--shadow);
  }
  .can-wrap--lime { left: 100px; }
  .can-wrap--night { left: 640px; }
  .can-wrap__art {
    position: absolute;
    inset: 0;
    width: 100%;
    height: 100%;
  }
  .brand-name {
    position: absolute;
    top: 92px;
    left: 40px;
    font-size: 104px;
    font-weight: 500;
    line-height: 1;
    letter-spacing: -1px;
  }
  .product-tag {
    position: absolute;
    top: 212px;
    left: 214px;
    padding: 7px 16px 7px 18px;
    border-radius: 0 16px 16px 0;
    color: var(--label-white);
    font-size: 17px;
    font-weight: 400;
    white-space: nowrap;
  }
  .volume {
    position: absolute;
    top: 270px;
    left: 262px;
    font-size: 46px;
    font-weight: 400;
  }
  .can-wrap--lime .brand-name,
  .can-wrap--lime .volume { color: var(--lime-green); }
  .can-wrap--lime .product-tag { background: var(--lime-green); }
  .can-wrap--night .brand-name,
  .can-wrap--night .volume { color: var(--navy); }
  .can-wrap--night .product-tag { background: var(--navy); }
</style>
</head>
<body>
<main class="canvas">

  <section class="can-wrap can-wrap--lime" aria-label="Veralo lime can wrap">
    <svg class="can-wrap__art" viewBox="0 0 460 640" preserveAspectRatio="none">
      <path class="accent-band" fill="var(--lime-band)"
            d="M0,200 Q70,430 460,440 L460,640 L0,640 Z"/>
      <path class="flavour-field" fill="var(--lime-green)" role="img"
            aria-label="Green field with a scattered pattern of lime leaves, drops and ice flakes"
            d="M0,236 Q80,458 460,470 L460,640 L0,640 Z"/>
    </svg>
    <div class="brand-name">Veralo</div>
    <div class="product-tag">Carbonated Soft Drink</div>
    <div class="volume">500ml</div>
  </section>

  <section class="can-wrap can-wrap--night" aria-label="Veralo night can wrap">
    <svg class="can-wrap__art" viewBox="0 0 460 640" preserveAspectRatio="none">
      <path class="accent-band" fill="var(--sky-band)"
            d="M0,200 Q70,430 460,440 L460,640 L0,640 Z"/>
      <path class="flavour-field" fill="var(--navy)"
            d="M0,222 Q80,452 460,458 L460,640 L0,640 Z"/>
    </svg>
    <div class="brand-name">Veralo</div>
    <div class="product-tag">Carbonated Soft Drink</div>
    <div class="volume">500ml</div>
  </section>

</main>
</body>
</html>
```